Hair & Skin Product Line

I need someone to design clear product labels that can go on pink bottles. I'm looking for someone who can add graphics such as avocado and honey to the label as these are ingredients in our products. The colors we want incorporated are gold, blue, white and purple. I will upload information about our company identity and information on one label. Whoever we choose, we will use them to create 11 more labels.

Target Market(s)

Woman 25-50, Natural, straight or curly hair.

Industry/Entity Type

Beauty

```html
<!DOCTYPE html>
<html lang="en">
<head>
<meta charset="utf-8">
<title>Avocado &amp; Honey Moisture Repair Shampoo – Label</title>
<link rel="stylesheet" href="https://fonts.googleapis.com/css2?family=Roboto+Condensed:wght@300;400&display=swap">
<style>
  :root {
    --backdrop: #3e3e42;
    --label-blue: #dcedf1;
    --label-edge: #c9e0e6;
    --ink: #3a3a3c;
    --brand-pink: #c8197a;
    --honey-light: #ffd21f;
    --honey-deep: #f0a81a;
  }
  * { margin: 0; padding: 0; box-sizing: border-box; }
  html, body {
    width: 1200px;
    height: 1149px;
    overflow: hidden;
    background: var(--backdrop);
  }
  .canvas {
    position: relative;
    width: 1200px;
    height: 1149px;
    background: var(--backdrop);
  }
  .label {
    position: absolute;
    left: 330px;
    top: 70px;
    width: 540px;
    height: 1010px;
    background: var(--label-blue);
    border: 1px solid var(--label-edge);
    display: flex;
    flex-direction: column;
    align-items: center;
    font-family: "Roboto Condensed", "Arial Narrow", sans-serif;
    color: var(--ink);
    text-align: center;
  }
  .label__art {
    margin-top: 70px;
    width: 340px;
    height: 330px;
    background: linear-gradient(160deg, var(--honey-light), var(--honey-deep));
  }
  .label__product {
    margin-top: 40px;
    font-weight: 300;
    font-size: 36px;
    line-height: 1.2;
  }
  .label__brand {
    margin-top: 56px;
    display: flex;
    align-items: center;
    gap: 14px;
    font-weight: 400;
    font-size: 54px;
    line-height: 1.1;
    color: var(--brand-pink);
  }
  .label__brand-dot {
    width: 22px;
    height: 22px;
    border-radius: 50%;
    background: var(--honey-light);
  }
  .label__claim {
    margin-top: 48px;
    font-weight: 300;
    font-size: 25px;
    line-height: 1.35;
  }
  .label__volume {
    margin-top: auto;
    margin-bottom: 90px;
    font-weight: 300;
    font-size: 28px;
  }
</style>
</head>
<body>
  <main class="canvas">
    <section class="label">
      <div class="label__art" role="img" aria-label="Illustration area: halved avocado with dripping honey on a golden honeycomb"></div>
      <h1 class="label__product">Avocado &amp; Honey<br>Moisture Repair Shampoo</h1>
      <p class="label__brand"><span>Velvet Grove</span><span class="label__brand-dot"></span></p>
      <p class="label__claim">Infused w/Biotin + Rosemary Gently<br>cleanses and hydrates&nbsp; for retention,</p>
      <p class="label__volume">300 ml /10 fl oz</p>
    </section>
  </main>
</body>
</html>
```